Pharmacy ad

need 2 pharmacy ads for the phone book. one for Birchfield Pharmacy and one for Corvane Rx Pharmacy. Dimensions for ad is 4.75in x 4.667 in. please see attached examples of ad uploaded as well logos of each pharmacy

```html
<!DOCTYPE html>
<html lang="en">
<head>
<meta charset="utf-8">
<title>Birchfield Pharmacy – Phone Book Ad</title>
<link rel="stylesheet" href="https://fonts.googleapis.com/css2?family=Montserrat:wght@700;800&family=Titillium+Web:ital,wght@0,400;0,600;1,400;1,600;1,700&family=PT+Sans:wght@700&display=swap">
<style>
:root{
  --navy:#2d2b45;
  --leaf:#6aa84f;
  --green-dark:#3f9e06;
  --green-light:#8cc63f;
  --orange:#ff8a00;
  --orange-light:#ffb000;
  --blue-a:#12c6f4;
  --blue-b:#8ef2ff;
  --lime-a:#96cf34;
  --lime-b:#d4f767;
  --lavender:#9b8cf5;
  --red:#e8101e;
  --white:#ffffff;
}
*{margin:0;padding:0;box-sizing:border-box}
html,body{width:1200px;height:1180px;overflow:hidden;background:#fff}
.ad{position:relative;width:1200px;height:1180px;overflow:hidden;font-family:"Titillium Web",sans-serif;color:var(--navy)}
.backdrop{position:absolute;inset:0 0 89px 0;
  background:
    radial-gradient(ellipse 420px 160px at 900px 540px, rgba(245,160,40,.35), transparent 70%),
    radial-gradient(ellipse 500px 200px at 300px 530px, rgba(120,150,200,.25), transparent 70%),
    linear-gradient(180deg,#f2f4f5 0%,#eef1f3 40%,#e4e8ec 60%,#eef0f2 100%)}
.brand{position:absolute;left:60px;top:70px;width:270px;text-align:center}
.brand-dot{width:64px;height:64px;border-radius:50%;background:var(--leaf);margin:0 auto 20px}
.brand-name{font-family:"Montserrat",sans-serif;font-weight:800;font-size:40px;line-height:1.05;color:var(--navy)}
.brand-tag{margin-top:14px;font-size:16px;color:var(--leaf);font-style:italic}
.headline{position:absolute;left:372px;top:84px;font-family:"Montserrat",sans-serif;font-weight:800;font-size:84px;line-height:.93;letter-spacing:1px}
.headline .top{color:var(--leaf)}
.headline .bottom{color:var(--navy)}
.discount{position:absolute;left:380px;top:282px;text-align:center;width:270px}
.discount .pct{font-family:"Montserrat",sans-serif;font-weight:800;font-size:142px;line-height:1;letter-spacing:-4px;
  background:linear-gradient(180deg,var(--orange-light),var(--orange));-webkit-background-clip:text;background-clip:text;color:transparent}
.discount .on{font-weight:700;font-style:italic;font-size:40px;line-height:1;color:var(--orange);margin-top:-4px}
.tag{position:absolute;left:671px;color:var(--white);font-style:italic;line-height:.95;padding:6px 0 0 22px}
.tag b{display:block;font-weight:700;font-size:29px}
.tag span{display:block;font-size:29px}
.tag-senior{top:304px;width:410px;height:66px;background:var(--green-dark);clip-path:polygon(0 0,100% 0,93% 100%,0 100%)}
.tag-student{top:376px;width:288px;height:66px;background:var(--green-light);clip-path:polygon(0 0,100% 0,80% 100%,0 100%)}
.feature{position:absolute;height:105px;display:flex;align-items:center;justify-content:center;text-align:center;
  font-family:"PT Sans",sans-serif;font-weight:700;font-size:27px;line-height:1;letter-spacing:1.5px;color:#10121c}
.feature.blue{background:linear-gradient(180deg,var(--blue-a),var(--blue-b))}
.feature.lime{background:linear-gradient(180deg,var(--lime-a),var(--lime-b))}
.hours{position:absolute;top:874px;font-style:italic;font-size:31px;line-height:.95}
.hours b{display:block;font-weight:700}
.hours span{display:block;font-weight:600;color:var(--navy)}
.band{position:absolute;left:0;top:978px;width:1200px;height:113px;background:linear-gradient(90deg,var(--orange),var(--orange-light) 48%,var(--orange) 50%,var(--orange-light) 65%,var(--orange))}
.band .divider{position:absolute;left:598px;top:0;width:3px;height:100%;background:var(--white)}
.branch{position:absolute;color:var(--white);font-style:italic;line-height:.95}
.branch b{display:block;font-weight:700;font-size:28px}
.branch small{display:block;font-size:20px;margin-top:2px}
.phone{position:absolute;top:18px;display:flex;align-items:center;gap:22px;font-family:"Montserrat",sans-serif;font-weight:700;font-size:60px;color:var(--white)}
.phone svg{width:44px;height:44px}
.footer{position:absolute;left:0;top:1091px;width:1200px;height:89px;background:var(--white);display:flex;align-items:center;padding:0 21px;font-size:24px;font-style:italic}
.accept{display:flex;align-items:center;gap:22px}
.accept .pay{font-style:normal;font-weight:700;color:var(--navy)}
.social{margin-left:auto;display:flex;align-items:center;gap:10px}
.social i{display:inline-block;width:30px;height:30px;background:var(--navy)}
.social b{font-weight:700}
</style>
</head>
<body>
<div class="ad">
  <div class="backdrop" role="img" aria-label="Softly blurred pharmacy interior with shelves of products"></div>

  <div class="brand">
    <div class="brand-dot"></div>
    <div class="brand-name">BIRCHFIELD<br>PHARMACY</div>
    <div class="brand-tag">We Care About Your Health</div>
  </div>

  <h1 class="headline"><div class="top">WE CARE ABOUT</div><div class="bottom">YOUR HEALTH</div></h1>

  <div class="discount">
    <div class="pct">10%</div>
    <div class="on">DISCOUNT ON</div>
  </div>
  <div class="tag tag-senior"><b>Senior Citizen discount</b><span>for patients 60 years &amp; over</span></div>
  <div class="tag tag-student"><b>Student discount</b><span>with valid ID card</span></div>

  <div class="feature blue" style="left:0;top:597px;width:295px">Certified<br>Pharmacists</div>
  <div class="feature lime" style="left:301px;top:597px;width:295px">Affordable<br>prices</div>
  <div class="feature blue" style="left:602px;top:597px;width:295px">Brand &amp; Generic<br>Medicines</div>
  <div class="feature lime" style="left:903px;top:597px;width:297px">Blood Pressure &amp;<br>Glucose checks</div>
  <div class="feature blue" style="left:151px;top:709px;width:295px">Personal care &amp;<br>Beauty Products</div>
  <div class="feature lime" style="left:452px;top:709px;width:295px">Injectables</div>
  <div class="feature blue" style="left:754px;top:709px;width:294px">Special Orders</div>

  <div class="hours" style="left:87px;color:var(--lavender)"><b>Delivery</b><b>Service</b></div>
  <div class="hours" style="left:292px"><b style="color:var(--green-dark)">Monday to Friday</b><span>10am- 6pm</span></div>
  <div class="hours" style="left:631px"><b style="color:var(--orange)">Saturday</b><span>10am-5pm</span></div>
  <div class="hours" style="left:880px"><b style="color:var(--red)">Sunday 10am-2pm</b><span style="font-weight:400">(Marlow Street branch)</span></div>

  <div class="band">
    <div class="branch" style="left:25px;top:12px"><b>27 Marlow Street,</b><b>Eastbay</b><small>(opposite Grace Hill<br>Chapel)</small></div>
    <div class="phone" style="left:232px">
      <svg viewBox="0 0 24 24" aria-hidden="true"><path fill="#e25a12" d="M6.6 10.8a15.1 15.1 0 0 0 6.6 6.6l2.2-2.2c.3-.3.7-.4 1-.2 1.1.4 2.3.6 3.6.6.6 0 1 .4 1 1V20c0 .6-.4 1-1 1C10.6 21 3 13.4 3 4c0-.6.4-1 1-1h3.5c.6 0 1 .4 1 1 0 1.3.2 2.5.6 3.6.1.3 0 .7-.2 1z"/></svg>
      555-0174
    </div>
    <div class="divider"></div>
    <div class="branch" style="left:640px;top:18px"><b>Harbour Point,</b><b>Food Court</b><b>Eastbay</b></div>
    <div class="phone" style="left:830px">
      <svg viewBox="0 0 24 24" aria-hidden="true"><path fill="#e25a12" d="M6.6 10.8a15.1 15.1 0 0 0 6.6 6.6l2.2-2.2c.3-.3.7-.4 1-.2 1.1.4 2.3.6 3.6.6.6 0 1 .4 1 1V20c0 .6-.4 1-1 1C10.6 21 3 13.4 3 4c0-.6.4-1 1-1h3.5c.6 0 1 .4 1 1 0 1.3.2 2.5.6 3.6.1.3 0 .7-.2 1z"/></svg>
      555-0177
    </div>
  </div>

  <div class="footer">
    <div class="accept">
      <span>We accept</span>
      <span class="pay">Paycard</span>
      <span class="pay">Vantra</span>
      <span class="pay">Sealine</span>
      <span class="pay">Harbor Insurances</span>
    </div>
    <div class="social"><span>Visit us on</span><i></i><b>Birchfield Rx Online</b></div>
  </div>
</div>
</body>
</html>
```